Sundial Bail Bonds Signboard Ad

I need a signboard ad that will be posted at a jail. We are a bail bond company and we bail people out of jail. The inmate/customer will call our company when they see our signboard ad posted inside a jail. The goal of the signboard ad is to get the attention of a person in custody and to stand out from the competition. The signboard ad is about 5x7. Open to any colors that will make it stand out. The content of the signboard ad must have "Sundial Bail Bonds" and our company phone number: (555) 318-2746. We want to emphasize we can get them out of jail quick and fast, was thinking maybe a catch phrase of "Sundial outta Jail" or "Sundial to Freedom". We don't have a logo. I will upload an attachment to show what the competition looks like. As you will see in the upload, my ad will go along with my competition. Also, I'm open to any creative ideas that will make my signboard ad stand out. Thank You.

Target Market(s)

People in jail.

Requirements
Must have
• Sundial Bail Bonds

(555) 318-2746
Nice to have
• I'm open to catch phrases that will get attention, for example "Sundial outta Jail" or "Sundial to Freedom". I do not have a company logo, if you can create a company logo, would be nice, was thinking an image of a rocket blasting off, The name of company is Sundial Bail Bonds.

```html
<!DOCTYPE html>
<html lang="en">
<head>
<meta charset="utf-8">
<title>Sundial Bail Bonds Signboard</title>
<link rel="stylesheet" href="https://fonts.googleapis.com/css2?family=Montserrat:ital,wght@0,600;0,700;0,800;1,900&display=swap">
<style>
  :root {
    --header-blue: #2a5b8f;
    --sky-top: #2f64a0;
    --sky-mid: #3f7dbb;
    --cloud: #e6ecf2;
    --pill-blue: #1173df;
    --pill-shadow: #0f1d2b;
    --teal: #16e0d2;
    --footer-cyan: #85dfe5;
    --ink: #1a1718;
    --white: #ffffff;
  }
  * { margin: 0; padding: 0; box-sizing: border-box; }
  html, body {
    width: 877px; height: 1200px; overflow: hidden;
    background: #ffffff;
    font-family: "Montserrat", Arial, sans-serif;
  }
  .signboard {
    position: relative;
    width: 877px; height: 1200px;
    background: var(--header-blue);
    overflow: hidden;
  }
  .photo-area {
    position: absolute;
    left: 0; top: 250px; width: 877px; height: 676px;
    background: linear-gradient(180deg, var(--header-blue) 0%, var(--sky-top) 25%, var(--sky-mid) 62%, #9fbbd6 80%, var(--cloud) 100%);
  }
  .brand-title {
    position: absolute;
    left: 0; top: 28px; width: 877px;
    text-align: center;
    color: var(--white);
    font-weight: 900; font-style: italic;
    font-size: 112px; line-height: 112px;
    letter-spacing: -1px;
    text-shadow: 4px 8px 10px rgba(5, 20, 40, 0.75);
  }
  .tag-pill {
    position: absolute;
    top: 282px; height: 47px;
    background: var(--pill-blue);
    color: var(--white);
    font-weight: 600; font-size: 24px; line-height: 47px;
    box-shadow: 3px 5px 0 var(--pill-shadow);
  }
  .tag-pill.left { left: 0; width: 405px; border-radius: 0 24px 24px 0; padding-left: 55px; }
  .tag-pill.right { right: 0; width: 335px; border-radius: 24px 0 0 24px; padding-left: 30px; box-shadow: -3px 5px 0 var(--pill-shadow); }
  .slogan {
    position: absolute;
    left: 0; top: 520px; width: 877px;
    text-align: center;
    color: var(--teal);
    font-weight: 700;
    font-size: 80px; line-height: 82px;
  }
  .slogan .second { display: block; }
  .slogan .first { display: block; padding-left: 30px; }
  .contact-band {
    position: absolute;
    left: 0; top: 926px; width: 877px; height: 274px;
    background: var(--footer-cyan);
  }
  .call-pill {
    position: absolute;
    left: 288px; top: 25px; width: 292px; height: 65px;
    border-radius: 33px;
    background: var(--pill-blue);
    box-shadow: 7px 8px 0 var(--pill-shadow);
    color: var(--white);
    font-weight: 700; font-size: 46px; line-height: 65px;
    text-align: center;
  }
  .phone {
    position: absolute;
    left: 0; top: 112px; width: 877px;
    text-align: center;
    color: var(--ink);
    font-weight: 800; font-size: 110px; line-height: 120px;
    letter-spacing: -3px;
  }
</style>
</head>
<body>
  <main class="signboard">
    <div class="photo-area" role="img" aria-label="Photo of two raised arms breaking free from open handcuffs against a blue sky with white clouds"></div>

    <h1 class="brand-title">SUNDIAL<br>BAIL BONDS</h1>

    <div class="tag-pill left">Same Day Bail Bonds</div>
    <div class="tag-pill right">Same Day Release</div>

    <p class="slogan"><span class="first">SUNDIAL</span><span class="second">TO FREEDOM</span></p>

    <section class="contact-band">
      <div class="call-pill">CALL US</div>
      <p class="phone">(555) 318-2746</p>
    </section>
  </main>
</body>
</html>
```